I need a simple infographic that describes the 4 basic elements of how to effectively create change.

The overall title (Gentle Pressure Relentlessly Applied) should be at the top of the infographic. Subtitle is: "Leading Change".
There are four steps:
1. Alignment- Agreement on Approach
2. Transparency- Metrics for Assurance
3. Skills- Training and Coaching
4. Integrity- Culture of Accountability

Target Market(s)

Business Leaders in a training workshop

Font styles to use
Serif

Requirements
Must have
• Here are the 4 elements of the Infographic: Please show them in order.
• 1. Agreement on Approach. (Alignment)
• 2. Metrics for Assurance (Transparency)
• 3. Training and Coaching (Skills)
• 4. Culture of Accountability (Integrity)
Nice to have
• Cool Graphics that depict the 4 steps.
Should not have
• Pictures.

```html
<!DOCTYPE html>
<html lang="en">
<head>
<meta charset="utf-8">
<title>Gentle Pressure Relentlessly Applied — Leading Change</title>
<link rel="stylesheet" href="https://fonts.googleapis.com/css2?family=Roboto:wght@300;700&family=PT+Sans:wght@400;700&display=swap">
<style>
  :root {
    --stage: #767676;
    --blue-light: #3cc4e8;
    --blue-mid: #2ea8dd;
    --blue-deep: #1b6fc2;
    --accent: #29a9e0;
    --band: #323232;
    --numeral: #555555;
    --ink: #111111;
    --white: #ffffff;
    --ring-grey-a: #e2e2e2;
    --ring-grey-b: #9a9a9a;
  }
  * { box-sizing: border-box; margin: 0; padding: 0; }
  html, body { width: 1153px; height: 1200px; overflow: hidden; }
  body { background: var(--stage); font-family: "PT Sans", sans-serif; position: relative; }

  .panel {
    position: absolute;
    overflow: hidden;
    box-shadow: 0 8px 22px rgba(0,0,0,.35);
  }
  .panel--blue {
    left: 35px; top: 35px; width: 1076px; height: 553px;
    background:
      radial-gradient(ellipse 60% 80% at 15% 100%, rgba(80,215,240,.55), transparent 70%),
      radial-gradient(ellipse 50% 70% at 100% 100%, rgba(20,90,190,.7), transparent 70%),
      linear-gradient(135deg, var(--blue-light) 0%, var(--blue-mid) 50%, var(--blue-deep) 100%);
  }
  .panel--white {
    left: 37px; top: 611px; width: 1072px; height: 542px;
    background: var(--white);
  }

  .brand {
    position: absolute; left: 0; right: 0; top: 26px;
    text-align: center;
    font-family: "Roboto", sans-serif; font-weight: 300;
    font-size: 48px; line-height: 1; color: var(--white); letter-spacing: -0.5px;
  }

  .title {
    position: absolute; left: 0; right: 0; text-align: center;
    font-family: "Roboto", sans-serif; font-weight: 700;
    font-size: 40px; line-height: 1; letter-spacing: .3px;
  }
  .subtitle {
    position: absolute; left: 0; right: 0; text-align: center;
    font-family: "Roboto", sans-serif; font-weight: 300;
    font-size: 30px; line-height: 1; letter-spacing: 2px;
  }
  .panel--blue .title { top: 106px; color: var(--white); padding-left: 30px; }
  .panel--blue .subtitle { top: 143px; color: var(--white); }
  .panel--white .title { top: 75px; color: var(--accent); }
  .panel--white .subtitle { top: 117px; color: #333; }

  .band {
    position: absolute; left: 0; right: 0; height: 100px;
    background: var(--band);
  }
  .panel--blue .band { top: 307px; }
  .panel--white .band { top: 277px; }

  .step { position: absolute; width: 0; height: 0; }
  .step__num {
    position: absolute; top: 0; transform: translate(-50%, -52%);
    font-family: "PT Sans", sans-serif; font-weight: 700;
    font-size: 62px; color: var(--numeral);
  }
  .step__ring {
    position: absolute; left: -68px; top: -76px;
    width: 150px; height: 150px; border-radius: 50%;
  }
  .panel--blue .step__ring {
    background: radial-gradient(circle at 35% 30%, var(--ring-grey-a), var(--ring-grey-b) 80%);
    box-shadow: 2px 4px 10px rgba(0,0,0,.35);
  }
  .panel--white .step__ring {
    background: radial-gradient(circle at 35% 30%, #3cc6f0, #1690d6 80%);
    box-shadow: 2px 4px 10px rgba(0,0,0,.25);
  }
  .step__disc {
    position: absolute; left: -55px; top: -55px;
    width: 110px; height: 110px; border-radius: 50%;
    background: radial-gradient(circle at 40% 35%, #ffffff 40%, #d8d8d8 100%);
    box-shadow: 3px 5px 10px rgba(0,0,0,.4);
    display: flex; align-items: center; justify-content: center;
  }
  .step__icon { width: 66px; height: 66px; fill: none; stroke: var(--ink); stroke-width: 2.2; stroke-linecap: round; stroke-linejoin: round; }

  .label {
    position: absolute; transform: translateX(-50%); white-space: nowrap;
    font-family: "PT Sans", sans-serif; color: var(--ink);
  }
  .label--key { font-weight: 700; font-size: 25px; }
  .label--note { font-weight: 700; font-size: 15.5px; }
  .panel--blue .label--key { color: var(--white); }
  .panel--white .label--key { color: var(--accent); }
</style>
</head>
<body>

<section class="panel panel--blue">
  <div class="brand">ORVANTEL WORKS</div>
  <h1 class="title">GENTLE PRESSURE RELENTLESSLY APPLIED</h1>
  <p class="subtitle">LEADING CHANGE</p>
  <div class="band"></div>

  <span class="label label--key" style="left:196px;top:238px">Alignment</span>
  <span class="label label--note" style="left:396px;top:248px">Metrics for Assurance</span>
  <span class="label label--key" style="left:597px;top:238px">Skills</span>
  <span class="label label--note" style="left:791px;top:246px">Culture of Accountability</span>

  <div class="step" style="left:201px;top:357px">
    <span class="step__num" style="left:-90px">1</span>
    <span class="step__ring"></span>
    <div class="step__disc">
      <svg class="step__icon" viewBox="0 0 64 64"><path d="M4 20l12-2 8 6 10-4 10 4 12-4 4 2v18l-6 2-12 10-8 4-6-4-8-6-10-6-6 0z"/><path d="M24 24l-6 8 4 4 10-6 6 6M26 42l4 4M32 38l6 6M38 34l6 6"/></svg>
    </div>
  </div>
  <div class="step" style="left:398px;top:357px">
    <span class="step__num" style="left:-94px">2</span>
    <span class="step__ring"></span>
    <div class="step__disc">
      <svg class="step__icon" viewBox="0 0 64 64"><circle cx="26" cy="26" r="18"/><circle cx="26" cy="26" r="13"/><path d="M15 26q11-10 22 0q-11 10-22 0z"/><circle cx="26" cy="26" r="3.5"/><path d="M39 39l6 6M44 42l12 12-4 4-12-12z"/></svg>
    </div>
  </div>
  <div class="step" style="left:597px;top:357px">
    <span class="step__num" style="left:-96px">3</span>
    <span class="step__ring"></span>
    <div class="step__disc">
      <svg class="step__icon" viewBox="0 0 64 64"><rect x="28" y="6" width="32" height="24" rx="2"/><circle cx="16" cy="14" r="6"/><path d="M8 44V28q0-6 8-6h4l14-8M20 30v28M14 44v14M8 44h6M20 30l10-4"/></svg>
    </div>
  </div>
  <div class="step" style="left:795px;top:357px">
    <span class="step__num" style="left:-95px">4</span>
    <span class="step__ring"></span>
    <div class="step__disc">
      <svg class="step__icon" viewBox="0 0 64 64"><circle cx="32" cy="9" r="3"/><path d="M32 12v40M10 18h44M14 18l-8 18h16zM50 18l-8 18h16zM6 36q8 8 16 0M42 36q8 8 16 0M22 54h20M26 58h12M30 52h4"/></svg>
    </div>
  </div>

  <span class="label label--note" style="left:200px;top:448px">Agreement on Approach</span>
  <span class="label label--key" style="left:403px;top:442px">Transparency</span>
  <span class="label label--note" style="left:603px;top:450px">Training and Coaching</span>
  <span class="label label--key" style="left:796px;top:442px">Integrity</span>
</section>

<section class="panel panel--white">
  <h2 class="title">GENTLE PRESSURE RELENTLESSLY APPLIED</h2>
  <p class="subtitle">LEADING CHANGE</p>
  <div class="band"></div>

  <span class="label label--key" style="left:191px;top:208px">Alignment</span>
  <span class="label label--note" style="left:390px;top:217px">Metrics for Assurance</span>
  <span class="label label--key" style="left:590px;top:208px">Skills</span>
  <span class="label label--note" style="left:785px;top:216px">Culture of Accountability</span>

  <div class="step" style="left:194px;top:327px">
    <span class="step__num" style="left:-88px">1</span>
    <span class="step__ring"></span>
    <div class="step__disc">
      <svg class="step__icon" viewBox="0 0 64 64"><path d="M4 20l12-2 8 6 10-4 10 4 12-4 4 2v18l-6 2-12 10-8 4-6-4-8-6-10-6-6 0z"/><path d="M24 24l-6 8 4 4 10-6 6 6M26 42l4 4M32 38l6 6M38 34l6 6"/></svg>
    </div>
  </div>
  <div class="step" style="left:392px;top:327px">
    <span class="step__num" style="left:-94px">2</span>
    <span class="step__ring"></span>
    <div class="step__disc">
      <svg class="step__icon" viewBox="0 0 64 64"><circle cx="26" cy="26" r="18"/><circle cx="26" cy="26" r="13"/><path d="M15 26q11-10 22 0q-11 10-22 0z"/><circle cx="26" cy="26" r="3.5"/><path d="M39 39l6 6M44 42l12 12-4 4-12-12z"/></svg>
    </div>
  </div>
  <div class="step" style="left:589px;top:327px">
    <span class="step__num" style="left:-94px">3</span>
    <span class="step__ring"></span>
    <div class="step__disc">
      <svg class="step__icon" viewBox="0 0 64 64"><rect x="28" y="6" width="32" height="24" rx="2"/><circle cx="16" cy="14" r="6"/><path d="M8 44V28q0-6 8-6h4l14-8M20 30v28M14 44v14M8 44h6M20 30l10-4"/></svg>
    </div>
  </div>
  <div class="step" style="left:788px;top:327px">
    <span class="step__num" style="left:-95px">4</span>
    <span class="step__ring"></span>
    <div class="step__disc">
      <svg class="step__icon" viewBox="0 0 64 64"><circle cx="32" cy="9" r="3"/><path d="M32 12v40M10 18h44M14 18l-8 18h16zM50 18l-8 18h16zM6 36q8 8 16 0M42 36q8 8 16 0M22 54h20M26 58h12M30 52h4"/></svg>
    </div>
  </div>

  <span class="label label--note" style="left:193px;top:419px">Agreement on Approach</span>
  <span class="label label--key" style="left:396px;top:413px">Transparency</span>
  <span class="label label--note" style="left:596px;top:421px">Training and Coaching</span>
  <span class="label label--key" style="left:789px;top:413px">Integrity</span>
</section>

</body>
</html>
```